Book Cover Project

This is a printed journal front and back cover design. We like the current design, but it feels a little too flat / too simple.

NOTE: we are not looking for a total makeover, just a finishing / polishing of this cover.

Here is our other book cover: https://www.shelvorix.com/Mat-Studio-Blueprint-Calm-Days/dp/7390462815/ref=tmm_hrd_swatch_0?_encoding=UTF8&qid=&sr=
it's purple and yellow (mostly purple)
this one is yellow and we're thinking to add a purple bar at the bottom

Specs: 6 in x 9 in full bleed for print

```html
<!DOCTYPE html>
<html lang="en">
<head>
<meta charset="utf-8">
<title>Finding Distance Logbook – Cover</title>
<link href="https://fonts.googleapis.com/css2?family=Arimo:wght@400;700&display=swap" rel="stylesheet">
<style>
  :root {
    --paper: #ffffff;
    --sun: #fed700;
    --sun-deep: #f3c800;
    --violet: #4f51a3;
  }
  html, body {
    margin: 0;
    padding: 0;
    width: 800px;
    height: 1200px;
    overflow: hidden;
    background: var(--paper);
  }
  .cover {
    display: block;
    width: 800px;
    height: 1200px;
    font-family: "Arimo", Arial, sans-serif;
  }
  .cover-field { fill: var(--sun); }
  .title-light { fill: var(--violet); font-weight: 400; font-size: 116px; }
  .title-heavy { fill: var(--violet); font-weight: 700; font-size: 130px; }
  .tagline-strip { fill: var(--paper); }
  .tagline { fill: var(--violet); font-weight: 700; font-size: 32px; }
  .author-bar { fill: var(--violet); }
  .author-name { fill: var(--sun); font-weight: 400; font-size: 27px; }
</style>
</head>
<body>
<svg class="cover" viewBox="0 0 800 1200" xmlns="http://www.w3.org/2000/svg">
  <defs>
    <linearGradient id="curlShade" x1="0" y1="0" x2="1" y2="0">
      <stop offset="0" stop-color="#c9cacd"/>
      <stop offset="0.35" stop-color="#ffffff"/>
      <stop offset="0.75" stop-color="#fbf6dc"/>
      <stop offset="1" stop-color="#f1dc84"/>
    </linearGradient>
    <radialGradient id="curlGlow" cx="0.5" cy="0.5" r="0.5">
      <stop offset="0" stop-color="#ff9a00" stop-opacity="0.8"/>
      <stop offset="1" stop-color="#ff9a00" stop-opacity="0"/>
    </radialGradient>
    <linearGradient id="runnerTone" x1="0" y1="0" x2="0" y2="1">
      <stop offset="0" stop-color="#f4cf00"/>
      <stop offset="1" stop-color="#ecc600"/>
    </linearGradient>
  </defs>

  <rect class="cover-field" x="14" y="14" width="772" height="1172"/>

  <g class="title">
    <text class="title-light" x="148" y="449">F</text>
    <g class="title-runner" role="img" aria-label="Single-line drawing of a runner standing in for the letter I">
      <rect x="226" y="316" width="52" height="155" rx="18" fill="url(#runnerTone)"/>
    </g>
    <text class="title-light" x="292" y="449" textLength="373" lengthAdjust="spacingAndGlyphs">NDING</text>
    <text class="title-heavy" x="64" y="566" textLength="672" lengthAdjust="spacingAndGlyphs">DISTANCE</text>
    <text class="title-light" x="132" y="673" textLength="532" lengthAdjust="spacingAndGlyphs">LOGBOOK</text>
  </g>

  <g class="tagline-tear">
    <ellipse cx="327" cy="780" rx="10" ry="40" fill="url(#curlGlow)"/>
    <polygon class="tagline-strip"
      points="386,722 410,726 432,723 460,727 486,722 510,725 534,720 556,722 578,718 600,721 622,719 644,723 668,720 690,725 712,723 734,727 752,722 770,725 786,722
              786,800 770,797 752,801 732,798 712,802 690,800 668,804 646,801 622,806 598,803 574,808 550,805 524,810 500,808 476,813 452,810 428,815 404,812 386,815"/>
    <polygon points="326,719 338,716 350,711 362,713 374,708 386,712 392,720 392,826 380,824 368,828 356,825 344,828 332,826 326,822"
      fill="url(#curlShade)"/>
    <text class="tagline" x="405" y="786" textLength="318" lengthAdjust="spacingAndGlyphs">Move - Reflect - Grow</text>
  </g>

  <g class="author">
    <rect class="author-bar" x="225" y="1066" width="349" height="55"/>
    <text class="author-name" x="270" y="1103" textLength="261" lengthAdjust="spacingAndGlyphs">MARCUS HOLLANDER</text>
  </g>
</svg>
</body>
</html>
```